International Technology Company Needs Cover Design

My company needs a Cover Design for my Ride the Quiet Tide online course. This course explains and demonstrates Exponential Technology and its effects on the Business Landscape. It serves Small and Medium Business owners.
This can be thought of as a Book Cover, but there is no physical book. It is a cover for delivery online. It may never physically exist. Similarly, it does not have to be limited to paper dimensions. Two of my examples are included: one as a book and one on an Tablora. I like the Globe/Planet analogy to illustrate how it is RIDE the quiet tide. Please ask any questions. Thank you.
Target Market(s)
Small and Medium Business Owners of non-Internet-centric companies; predominantly male; 40-55 yrs old
Industry/Entity Type
It Company
Other font styles liked:
- Make it work with the Design Sliders above.
Requirements
Must have
- Authority; Fonts that can be used online for consistency; web/video applicable color palette; Sense of Possibility and Innovation; Same Title; open to other Subtitle suggestions.)
Nice to have
- Innovation. Unique thought. Progression of technology/business/possibility.
Should not have
- Different Title. (Other Subtitles may be suggested.)

```html
<!DOCTYPE html>
<html lang="en">
<head>
<meta charset="utf-8">
<title>Ride the Quiet Tide – Course Cover</title>
<link href="https://fonts.googleapis.com/css2?family=Oswald:wght@500;600&family=Montserrat:wght@900&display=swap" rel="stylesheet">
<style>
  :root {
    --page: #ffffff;
    --cover-deep: #0a2a6b;
    --cover-mid: #0b4f9e;
    --cover-glow: #1a7fc8;
    --title-muted: #7aa3b2;
    --title-bright: #f8f4f4;
    --subtitle: #9fcbd2;
    --author: #f4f6fa;
    --globe-light: #a9c7d3;
    --globe-dark: #3e5f78;
  }
  html, body {
    margin: 0;
    width: 1200px;
    height: 1059px;
    overflow: hidden;
    background: var(--page);
  }
  .canvas {
    position: relative;
    width: 1200px;
    height: 1059px;
  }
  .cover {
    position: absolute;
    left: 250px;
    top: 50px;
    width: 583px;
    height: 872px;
    overflow: hidden;
    background: radial-gradient(ellipse 75% 60% at 55% 55%, var(--cover-glow) 0%, var(--cover-mid) 45%, var(--cover-deep) 100%);
    text-align: center;
  }
  .title { margin: 0; font-weight: normal; }
  .title-line {
    position: absolute;
    left: 0;
    width: 100%;
    line-height: 1;
    white-space: nowrap;
  }
  .title-top {
    top: 5px;
    display: flex;
    justify-content: center;
    align-items: baseline;
    gap: 18px;
    color: var(--title-muted);
  }
  .title-top .accent {
    font-family: "Montserrat", sans-serif;
    font-weight: 900;
    font-size: 138px;
    letter-spacing: 1px;
  }
  .title-top .small {
    font-family: "Oswald", sans-serif;
    font-weight: 600;
    font-size: 75px;
  }
  .title-mid {
    top: 161px;
    font-family: "Oswald", sans-serif;
    font-weight: 600;
    font-size: 44px;
    color: var(--title-muted);
    letter-spacing: 1px;
  }
  .title-main {
    top: 190px;
    font-family: "Montserrat", sans-serif;
    font-weight: 900;
    font-size: 150px;
    color: var(--title-bright);
    letter-spacing: 2px;
  }
  .subtitle {
    position: absolute;
    top: 322px;
    left: 0;
    width: 100%;
    margin: 0;
    font-family: "Oswald", sans-serif;
    font-weight: 500;
    font-size: 26px;
    color: var(--subtitle);
    white-space: nowrap;
  }
  .subtitle .amp { font-size: 32px; margin: 0 10px; }
  .world-art {
    position: absolute;
    left: 0;
    top: 385px;
    width: 583px;
    height: 420px;
  }
  .author {
    position: absolute;
    left: 0;
    bottom: 9px;
    width: 100%;
    margin: 0;
    font-family: "Oswald", sans-serif;
    font-weight: 500;
    font-size: 50px;
    color: var(--author);
    letter-spacing: 1px;
  }
</style>
</head>
<body>
<div class="canvas">
  <section class="cover">
    <h1 class="title">
      <span class="title-line title-top"><span class="accent">RIDE</span><span class="small">THE</span></span>
      <span class="title-line title-mid">QUIET</span>
      <span class="title-line title-main">TIDE</span>
    </h1>
    <p class="subtitle">ACCELERATING INNOVATION<span class="amp">&amp;</span>MARKET HORIZONS</p>
    <svg class="world-art" viewBox="0 0 583 420" role="img" aria-label="Glass globe with binary code and glowing city lights over a world map of the continents">
      <defs>
        <radialGradient id="globe-fill" cx="45%" cy="35%" r="70%">
          <stop offset="0%" stop-color="var(--globe-light)"/>
          <stop offset="100%" stop-color="var(--globe-dark)"/>
        </radialGradient>
      </defs>
      <circle cx="320" cy="205" r="192" fill="url(#globe-fill)"/>
    </svg>
    <p class="author">GARY J MELVILLE JUNIOR</p>
  </section>
</div>
</body>
</html>
```